Brintell's Business Card

I need some designs for a new business card including the new logo attached. An old example of our business card is also attached to show all the data that should be included on the new design.
**I added some more examples someone had mocked up**

Contact Information for Business Card

Should include all info on other examples uploaded.

```html
<!DOCTYPE html>
<html lang="en">
<head>
<meta charset="utf-8">
<title>Brintell's Business Card</title>
<link href="https://fonts.googleapis.com/css2?family=Montserrat:wght@500;600;800&display=swap" rel="stylesheet">
<style>
  :root {
    --brand-blue: #0b6fb6;
    --brand-red: #e8212b;
    --paper: #ffffff;
    --backdrop: #e4e3e4;
  }
  * { margin: 0; padding: 0; box-sizing: border-box; }
  html, body { width: 1200px; height: 1200px; overflow: hidden; }
  body {
    background: var(--backdrop);
    font-family: "Montserrat", Arial, sans-serif;
    position: relative;
  }
  .card {
    position: absolute;
    left: 150px;
    width: 900px;
    height: 514px;
    background: var(--paper);
    overflow: hidden;
    box-shadow: 0 12px 30px rgba(0,0,0,0.18);
  }
  .card--front { top: 40px; }
  .card--back { top: 646px; }

  .band { position: absolute; left: 0; width: 900px; }
  .band svg { position: absolute; left: 0; top: 0; }
  .band__text {
    position: absolute; left: 0; right: 0;
    color: var(--paper);
    font-weight: 500;
    letter-spacing: 0.04em;
    text-transform: uppercase;
    text-align: center;
  }
  .band--top { top: 0; height: 117px; }
  .band--top .band__text { top: 22px; font-size: 31px; }
  .band--bottom { bottom: 0; height: 117px; }
  .band--bottom .band__text { top: 58px; font-size: 21px; }

  .wordmark { position: absolute; display: flex; align-items: center; }
  .wordmark__dot { border-radius: 50%; background: var(--brand-blue); flex: none; }
  .wordmark__name {
    color: var(--brand-blue);
    font-weight: 600;
    line-height: 1;
    letter-spacing: 0.01em;
  }
  .wordmark__tagline {
    color: var(--brand-red);
    font-weight: 600;
    text-transform: uppercase;
    letter-spacing: 0.03em;
    margin-top: 6px;
  }
  .card--front .wordmark { left: 170px; top: 196px; }
  .card--front .wordmark__dot { width: 96px; height: 96px; margin-right: 26px; }
  .card--front .wordmark__name { font-size: 90px; }
  .card--front .wordmark__tagline { font-size: 19.5px; }

  .card--back .wordmark { left: 470px; top: 54px; }
  .card--back .wordmark__dot { width: 58px; height: 58px; margin-right: 16px; }
  .card--back .wordmark__name { font-size: 52px; }
  .card--back .wordmark__tagline { font-size: 11.5px; margin-top: 4px; }

  .contact { position: absolute; left: 70px; top: 330px; }
  .contact__name {
    color: var(--brand-red);
    font-weight: 800;
    font-size: 40px;
    text-transform: uppercase;
    letter-spacing: 0.01em;
    margin-bottom: 10px;
  }
  .contact__line {
    display: flex; align-items: center;
    color: var(--brand-blue);
    font-size: 25px; font-weight: 500;
    line-height: 1.35;
  }
  .contact__line svg { margin-right: 12px; flex: none; }

  .credentials {
    position: absolute; right: 60px; top: 300px;
    color: var(--brand-blue);
    font-size: 25px; font-weight: 500;
    text-transform: uppercase;
    letter-spacing: 0.03em;
    line-height: 1.4;
  }
</style>
</head>
<body>

<section class="card card--front">
  <div class="band band--top">
    <svg width="900" height="117" viewBox="0 0 900 117">
      <path d="M0 0H900V92H430L400 117L370 92H0Z" fill="var(--brand-blue)"/>
    </svg>
    <p class="band__text">Serves Millbrook, IA &amp; Surrounding Areas</p>
  </div>

  <div class="wordmark">
    <span class="wordmark__dot"></span>
    <div>
      <div class="wordmark__name">BRINTELL'S</div>
      <div class="wordmark__tagline">Air Conditioning &amp; Heating Service</div>
    </div>
  </div>

  <div class="band band--bottom">
    <svg width="900" height="117" viewBox="0 0 900 117">
      <path d="M0 25H310L340 0L370 25H900V117H0Z" fill="var(--brand-red)"/>
    </svg>
    <p class="band__text">Call today for all your HVAC, refrigeration &amp; plumbing needs</p>
  </div>
</section>

<section class="card card--back">
  <div class="wordmark">
    <span class="wordmark__dot"></span>
    <div>
      <div class="wordmark__name">BRINTELL'S</div>
      <div class="wordmark__tagline">Air Conditioning &amp; Heating Service</div>
    </div>
  </div>

  <div class="contact">
    <p class="contact__name">Dale Morrow</p>
    <p class="contact__line">
      <svg width="20" height="20" viewBox="0 0 24 24" aria-hidden="true">
        <path d="M6.6 10.8a15 15 0 0 0 6.6 6.6l2.2-2.2a1 1 0 0 1 1-.25 11.4 11.4 0 0 0 3.6.57 1 1 0 0 1 1 1V20a1 1 0 0 1-1 1A17 17 0 0 1 3 4a1 1 0 0 1 1-1h3.5a1 1 0 0 1 1 1c0 1.25.2 2.45.57 3.57a1 1 0 0 1-.25 1Z" fill="var(--brand-red)"/>
      </svg>
      555.014.2291
    </p>
    <p class="contact__line">
      <svg width="20" height="20" viewBox="0 0 24 24" aria-hidden="true">
        <rect x="2" y="5" width="20" height="14" rx="1.5" fill="var(--brand-red)"/>
        <path d="M3 6.5l9 6.5 9-6.5" fill="none" stroke="#fff" stroke-width="1.6"/>
      </svg>
      hvacbrintell@mailbox.com
    </p>
  </div>

  <div class="credentials">
    <p>Licensed &amp; Insured</p>
    <p>Family Owned &amp; Operated</p>
  </div>
</section>

</body>
</html>
```